Marlowe Fen Gin (bottle label)

Marlowe Fen Gin is a hand crafted spirit distilled by Tidewell Distillery. The distillery is farm based. This is our first offering. The label is to be applied to a glass bottle.

We chose the name because we felt lucky to chance upon a great recipe. So we came up with Marlowe Fen Gin. The phrase "Sometimes you get lucky" needs to be included. We'd like to see imagery of a lucky symbol such as a 4 leaf clover or shooting star. Elegant contrast come to mind. Reference to the distillery, bottle size (375ml) and Alc./vol. 40% is also needed. The distillery logo could be included. Or all is included in printed content.
Logo included for reference.
The label is rectangular.

Target Market(s)

Adults who enjoy fine spirits

Industry/Entity Type

Spirits distillation

Font styles to use
Serif
Script

Requirements
Must have
• classy, eye catching presentation
Nice to have
• Stylized 4 leaf clover or shooting star
Should not have
• Nothing hokey

```html
<!DOCTYPE html>
<html lang="en">
<head>
<meta charset="utf-8">
<title>Marlowe Fen Gin — Bottle Label</title>
<link rel="stylesheet" href="https://fonts.googleapis.com/css2?family=Poppins:wght@300;400;500&family=Yellowtail&display=swap">
<style>
  :root {
    --backdrop: #cfcfcf;
    --label: #f7f7f7;
    --label-edge: #e2e2e2;
    --grey-ink: #6e6e6e;
    --grey-soft: #8a8a8a;
    --green-deep: #2f6b1f;
    --green-mid: #4f9a2a;
    --green-bright: #7cc946;
    --bar-top: #4a9a24;
    --bar-bottom: #2d6b17;
    --white: #ffffff;
  }
  * { margin: 0; padding: 0; box-sizing: border-box; }
  html, body {
    width: 1200px;
    height: 1200px;
    overflow: hidden;
    background: var(--backdrop);
  }
  .label {
    position: absolute;
    left: 280px;
    top: 120px;
    width: 640px;
    height: 960px;
    background: var(--label);
    border: 2px solid var(--label-edge);
    border-radius: 22px;
    box-shadow: 0 6px 24px rgba(0,0,0,0.12);
    overflow: hidden;
  }
  .distillery {
    position: absolute;
    top: 112px;
    left: 0;
    width: 100%;
    text-align: center;
    font-family: "Poppins", sans-serif;
    font-weight: 400;
    font-size: 26px;
    line-height: 40px;
    letter-spacing: 3px;
    color: var(--grey-ink);
    white-space: nowrap;
  }
  .product-name {
    position: absolute;
    top: 296px;
    left: 0;
    width: 100%;
    height: 120px;
    text-align: center;
    font-family: "Yellowtail", cursive;
    font-weight: 400;
    font-size: 100px;
    line-height: 120px;
    white-space: nowrap;
    background: linear-gradient(90deg, var(--green-deep) 0%, var(--green-mid) 45%, var(--green-bright) 75%, var(--green-deep) 100%);
    -webkit-background-clip: text;
    background-clip: text;
    color: transparent;
  }
  .spirit-type {
    position: absolute;
    top: 432px;
    left: 0;
    width: 100%;
    height: 56px;
    display: flex;
    align-items: center;
    justify-content: center;
    gap: 18px;
  }
  .spirit-type .word {
    font-family: "Poppins", sans-serif;
    font-weight: 300;
    font-size: 44px;
    line-height: 56px;
    letter-spacing: 16px;
    margin-right: -16px;
    color: var(--grey-ink);
    white-space: nowrap;
  }
  .spirit-type svg { display: block; }
  .lucky-symbol {
    position: absolute;
    top: 522px;
    left: 222px;
    width: 196px;
    height: 196px;
    border-radius: 50%;
    background: radial-gradient(circle, var(--green-deep) 0%, var(--green-mid) 45%, rgba(124,201,70,0.35) 70%, rgba(124,201,70,0) 72%);
  }
  .tagline {
    position: absolute;
    top: 738px;
    left: 0;
    width: 100%;
    text-align: center;
    font-family: "Yellowtail", cursive;
    font-size: 50px;
    line-height: 64px;
    color: var(--grey-soft);
    white-space: nowrap;
  }
  .spec-bar {
    position: absolute;
    top: 852px;
    left: 160px;
    width: 320px;
    height: 70px;
    border-radius: 8px;
    background: linear-gradient(180deg, var(--bar-top), var(--bar-bottom));
    display: flex;
    align-items: center;
    justify-content: center;
    gap: 14px;
    font-family: "Poppins", sans-serif;
    font-weight: 400;
    font-size: 22px;
    color: var(--white);
    white-space: nowrap;
  }
  .spec-bar .divider {
    width: 2px;
    height: 30px;
    background: var(--white);
  }
</style>
</head>
<body>
  <main class="label">
    <div class="distillery">Tidewell Distillery</div>
    <h1 class="product-name">Marlowe Fen</h1>
    <div class="spirit-type">
      <svg width="140" height="10" viewBox="0 0 140 10" aria-hidden="true">
        <polygon points="0,5 140,2 140,8" fill="#6e6e6e"/>
      </svg>
      <span class="word">GIN</span>
      <svg width="140" height="10" viewBox="0 0 140 10" aria-hidden="true">
        <polygon points="0,2 0,8 140,5" fill="#6e6e6e"/>
      </svg>
    </div>
    <div class="lucky-symbol" role="img" aria-label="Stylised green four-leaf clover emblem"></div>
    <p class="tagline">Sometimes you get lucky</p>
    <div class="spec-bar">
      <span>40% Alc./vol.</span>
      <span class="divider"></span>
      <span>375ml</span>
    </div>
  </main>
</body>
</html>
```